Merriwick Law - New Letterhead/Logo

Hello!
THE FIRM NAME IS NOW MERRIWICK LAW. We recently just changed our name and we are in need of a classy letterhead. Attached I have a logo we have included in the past, but we are willing to look at other alternatives as well. I will also attach our current letterhead with our old name, Merriwick & Associates. We are willing to go without attorney names. Please help! Thanks

```html
<!DOCTYPE html>
<html lang="en">
<head>
<meta charset="utf-8">
<title>Merriwick Law – Stationery</title>
<link href="https://fonts.googleapis.com/css2?family=Open+Sans:wght@400;600;700&display=swap" rel="stylesheet">
<style>
  :root{
    --stage:#e6e6e6;
    --paper:#ffffff;
    --brand:#1f7fc8;
    --brand-deep:#1a6fb0;
    --slate:#5d6f7e;
    --ink:#3a3a3a;
    --black:#111111;
    --cell-label:#d7dadd;
    --cell-value:#e8eaec;
  }
  *{box-sizing:border-box;margin:0;padding:0}
  html,body{width:1200px;height:520px;overflow:hidden}
  body{background:var(--stage);font-family:"Open Sans",Arial,sans-serif;position:relative;color:var(--ink)}
  .piece{position:absolute;background:var(--paper);box-shadow:0 1px 3px rgba(0,0,0,.25);overflow:hidden}

  /* Envelope back */
  .envelope-back{left:47px;top:113px;width:275px;height:133px}
  .envelope-back .flap{position:absolute;left:0;top:0;width:100%;height:47px;background:var(--brand);border-radius:0 0 12px 12px}

  /* Envelope front */
  .envelope-front{left:47px;top:273px;width:275px;height:134px}
  .brand-name{display:flex;align-items:center;gap:5px;color:var(--brand);font-weight:600;letter-spacing:.5px;white-space:nowrap}
  .brand-name .mark{display:block;background:var(--brand)}
  .envelope-front .brand-name{position:absolute;left:13px;top:23px;font-size:15px}
  .envelope-front .brand-name .mark{width:10px;height:10px}
  .envelope-front .return-address{position:absolute;left:13px;top:68px;font-size:6.5px;font-weight:600;line-height:9px;color:var(--black)}
  .swoosh{position:absolute;left:0;bottom:0;display:block}

  /* Letter sheets */
  .sheet{width:228px;height:362px}
  .letterhead{left:340px;top:78px}
  .fax-sheet{left:622px;top:80px;width:256px;height:362px}
  .sheet .brand-name{position:absolute;left:0;right:0;top:28px;justify-content:center;font-size:15px}
  .sheet .brand-name .mark{width:10px;height:10px}
  .recipient{position:absolute;left:21px;top:79px;font-size:4.3px;line-height:5.4px}
  .body-copy{position:absolute;left:21px;right:21px;font-size:4.1px;line-height:5.3px;text-align:justify}
  .body-copy p{margin-bottom:4px}
  .letterhead .body-copy{top:105px}
  .fax-sheet .body-copy{top:150px;left:18px;right:18px}
  .signature{position:absolute;font-size:11px;color:var(--brand);font-weight:400}
  .letterhead .signature{left:21px;top:270px}
  .fax-sheet .signature{left:22px;top:271px}
  .contact-list{position:absolute;right:10px;list-style:none;text-align:right;color:#fff;font-size:6.2px;font-weight:600;line-height:9.2px}
  .contact-list li{display:flex;justify-content:flex-end;align-items:center;gap:3px}
  .contact-list svg{width:5px;height:5px;display:block}
  .contact-list .address{font-size:6.2px}
  .letterhead .contact-list{top:296px}
  .fax-sheet .contact-list{top:294px}

  /* Fax header table */
  .fax-fields{position:absolute;left:16px;top:70px;width:222px;border-collapse:separate;border-spacing:2px 1px;font-size:3.8px;font-weight:700}
  .fax-fields td{height:11px;padding-left:2px}
  .fax-fields .label{background:var(--cell-label);width:30px}
  .fax-fields .value{background:var(--cell-value)}
  .fax-options{position:absolute;left:17px;top:121px;display:flex;gap:17px;font-size:3.6px;font-weight:600;list-style:none}
  .fax-options li{display:flex;align-items:center;gap:2px}
  .fax-options li::before{content:"";width:4px;height:4px;border:.5px solid var(--ink);background:#fff}

  /* Cover / folder */
  .cover{left:898px;top:80px;width:256px;height:360px;background:var(--brand)}
  .cover .watermark-name{position:absolute;left:0;right:0;top:95px;text-align:center;font-size:38px;font-weight:600;line-height:60px;color:rgba(255,255,255,.1);letter-spacing:2px}
  .cover .brand-name{position:absolute;right:14px;top:318px;color:#fff;font-size:15px}
  .cover .brand-name .mark{width:10px;height:10px;background:#fff}
</style>
</head>
<body>

<div class="piece envelope-back">
  <div class="flap"></div>
</div>

<div class="piece envelope-front">
  <div class="brand-name"><span class="mark"></span>MERRIWICK LAW</div>
  <div class="return-address">2250 Harbor Lane<br>Fairview, CA 95012</div>
  <svg class="swoosh" width="275" height="134" viewBox="0 0 275 134">
    <path d="M0,100 C80,122 170,40 275,18 L275,29 C170,55 90,128 0,112 Z" fill="var(--black)"/>
    <path d="M0,116 C90,132 180,62 275,38 L275,42 C180,70 90,136 0,121 Z" fill="var(--brand)"/>
    <path d="M0,124 C90,136 185,72 275,48 L275,134 L0,134 Z" fill="var(--brand)"/>
  </svg>
</div>

<div class="piece sheet letterhead">
  <div class="brand-name"><span class="mark"></span>MERRIWICK LAW</div>
  <div class="recipient">Client Name<br>Street Address<br>City, State</div>
  <div class="body-copy">
    <p>Thank you for your recent inquiry regarding our legal services and the matters we discussed during our meeting. Our team will review every document carefully and prepare a clear summary of your options before the next step.</p>
    <p>Our team will review every document carefully and prepare a clear summary of your options before the next step. Please contact our office with any questions, and we will respond promptly to schedule a convenient time. Thank you for your recent inquiry regarding our legal services and the matters we discussed during our meeting.</p>
    <p>Please contact our office with any questions, and we will respond promptly to schedule a convenient time. Thank you for your recent inquiry regarding our legal services and the matters we discussed during our meeting.</p>
    <p>Our team will review every document carefully and prepare a clear summary of your options before the next step.</p>
  </div>
  <div class="signature">Alex Carter</div>
  <svg class="swoosh" width="228" height="108" viewBox="0 0 228 108">
    <path d="M0,58 C70,90 150,30 228,2 L228,14 C150,40 70,100 0,70 Z" fill="var(--slate)"/>
    <path d="M0,76 C70,104 150,46 228,20 L228,24 C150,52 70,110 0,80 Z" fill="var(--brand)"/>
    <path d="M0,86 C70,110 150,56 228,30 L228,108 L0,108 Z" fill="var(--brand)"/>
  </svg>
  <ul class="contact-list">
    <li>(555) 204-7310 <svg viewBox="0 0 10 10"><path d="M2,1 L4,1 L5,3 L3.8,4.2 C4.5,5.6 5,6 6,6.4 L7,5 L9,6 L9,8 C5,9 1,5 2,1 Z" fill="#fff"/></svg></li>
    <li>(555) 204-7311 <svg viewBox="0 0 10 10"><path d="M2,1 L4,1 L5,3 L3.8,4.2 C4.5,5.6 5,6 6,6.4 L7,5 L9,6 L9,8 C5,9 1,5 2,1 Z" fill="#fff"/></svg></li>
    <li>(555) 318-4402 <svg viewBox="0 0 10 10"><rect x="2" y="1" width="6" height="8" rx="1" fill="#fff"/></svg></li>
    <li>contact@merriwicklaw.com <svg viewBox="0 0 10 10"><rect x="1" y="2" width="8" height="6" fill="#fff"/></svg></li>
    <li>www.merriwicklaw.com <svg viewBox="0 0 10 10"><circle cx="5" cy="5" r="4" fill="#fff"/></svg></li>
    <li class="address">2250 Harbor Lane, Fairview, CA 95012 <svg viewBox="0 0 10 10"><path d="M5,1 C7.5,1 8.5,3 8,4.5 L5,9 L2,4.5 C1.5,3 2.5,1 5,1 Z" fill="#fff"/></svg></li>
  </ul>
</div>

<div class="piece sheet fax-sheet">
  <div class="brand-name"><span class="mark"></span>MERRIWICK LAW</div>
  <table class="fax-fields">
    <tr><td class="label">TO</td><td class="value"></td><td class="label">FROM</td><td class="value"></td></tr>
    <tr><td class="label">FAX</td><td class="value"></td><td class="label">PAGES</td><td class="value"></td></tr>
    <tr><td class="label">PHONE</td><td class="value"></td><td class="label">DATE</td><td class="value"></td></tr>
    <tr><td class="label">RE</td><td class="value"></td><td class="label">CC</td><td class="value"></td></tr>
  </table>
  <ul class="fax-options">
    <li>Urgent</li><li>For Review</li><li>Please comment</li><li>Please reply</li><li>Please recycle</li>
  </ul>
  <div class="body-copy">
    <p>Thank you for your recent inquiry regarding our legal services and the matters we discussed during our meeting. Our team will review every document carefully and prepare a clear summary of your options before the next step.</p>
    <p>Our team will review every document carefully and prepare a clear summary of your options before the next step. Please contact our office with any questions, and we will respond promptly to schedule a convenient time. Thank you for your recent inquiry regarding our legal services and the matters we discussed during our meeting.</p>
    <p>Please contact our office with any questions, and we will respond promptly to schedule a convenient time.</p>
  </div>
  <div class="signature">Alex Carter</div>
  <svg class="swoosh" width="256" height="108" viewBox="0 0 256 108">
    <path d="M0,58 C80,90 170,30 256,2 L256,14 C170,40 80,100 0,70 Z" fill="var(--slate)"/>
    <path d="M0,76 C80,104 170,46 256,20 L256,24 C170,52 80,110 0,80 Z" fill="var(--brand)"/>
    <path d="M0,86 C80,110 170,56 256,30 L256,108 L0,108 Z" fill="var(--brand)"/>
  </svg>
  <ul class="contact-list">
    <li>(555) 204-7310 <svg viewBox="0 0 10 10"><path d="M2,1 L4,1 L5,3 L3.8,4.2 C4.5,5.6 5,6 6,6.4 L7,5 L9,6 L9,8 C5,9 1,5 2,1 Z" fill="#fff"/></svg></li>
    <li>(555) 204-7311 <svg viewBox="0 0 10 10"><path d="M2,1 L4,1 L5,3 L3.8,4.2 C4.5,5.6 5,6 6,6.4 L7,5 L9,6 L9,8 C5,9 1,5 2,1 Z" fill="#fff"/></svg></li>
    <li>(555) 318-4402 <svg viewBox="0 0 10 10"><rect x="2" y="1" width="6" height="8" rx="1" fill="#fff"/></svg></li>
    <li>contact@merriwicklaw.com <svg viewBox="0 0 10 10"><rect x="1" y="2" width="8" height="6" fill="#fff"/></svg></li>
    <li>www.merriwicklaw.com <svg viewBox="0 0 10 10"><circle cx="5" cy="5" r="4" fill="#fff"/></svg></li>
    <li class="address">2250 Harbor Lane, Fairview, CA 95012 <svg viewBox="0 0 10 10"><path d="M5,1 C7.5,1 8.5,3 8,4.5 L5,9 L2,4.5 C1.5,3 2.5,1 5,1 Z" fill="#fff"/></svg></li>
  </ul>
</div>

<div class="piece cover">
  <div class="watermark-name" aria-hidden="true">MERRIWICK<br>LAW</div>
  <div class="brand-name"><span class="mark"></span>MERRIWICK LAW</div>
</div>

</body>
</html>
```